Professional/Sleek card design for athletic apparel brand

Athletic apparel brand. Mainly focused on lifting weights/gym workouts. Logo and brand are already created. Must use brand logo and name. Creativity is welcome. Looking for a clean, modern, and sexy design.

```html
<!DOCTYPE html>
<html lang="en">
<head>
<meta charset="utf-8">
<title>Iron and Grit – Business Card</title>
<link rel="stylesheet" href="https://fonts.googleapis.com/css2?family=Montserrat:wght@400;600;800&display=swap">
<style>
  :root {
    --bg-top: #cfcfcf;
    --bg-bottom: #9d9d9d;
    --card: #262626;
    --card-back: #232323;
    --ink: #ffffff;
    --ink-soft: #d9d9d9;
    --rule: #7a7a7a;
    --mark-faint: #1d1d1d;
  }
  * { box-sizing: border-box; margin: 0; padding: 0; }
  html, body { width: 1200px; height: 802px; overflow: hidden; }
  body {
    background: linear-gradient(180deg, var(--bg-top), var(--bg-bottom));
    font-family: "Montserrat", sans-serif;
    color: var(--ink);
    display: flex;
    align-items: center;
    justify-content: center;
    gap: 40px;
  }
  .card {
    width: 540px;
    height: 309px;
    border-radius: 18px;
    background: var(--card);
    position: relative;
    overflow: hidden;
    box-shadow: 0 14px 30px rgba(0,0,0,.28);
  }

  /* front */
  .card-front { padding: 34px 30px 0; }
  .wordmark {
    display: flex;
    align-items: center;
    justify-content: center;
    gap: 14px;
  }
  .wordmark-dot {
    width: 22px; height: 22px;
    border-radius: 50%;
    background: var(--ink);
  }
  .wordmark-name {
    font-weight: 600;
    font-size: 15px;
    letter-spacing: 0.55em;
    margin-right: -0.55em;
  }
  .details {
    margin-top: 46px;
    display: flex;
    justify-content: center;
    align-items: center;
  }
  .person { text-align: right; padding-right: 20px; }
  .person-name { font-weight: 800; font-size: 19px; letter-spacing: .02em; }
  .person-role { font-weight: 400; font-size: 13px; color: var(--ink-soft); margin-top: 2px; }
  .divider { width: 1px; height: 66px; background: var(--rule); }
  .contact { list-style: none; padding-left: 20px; font-size: 13px; line-height: 1.75; }
  .contact li { display: flex; align-items: center; gap: 8px; }
  .contact svg { width: 11px; height: 11px; fill: var(--ink); flex: none; }
  .address {
    position: absolute;
    left: 0; right: 0; bottom: 42px;
    text-align: center;
    font-size: 13px;
    color: var(--ink-soft);
  }

  /* back */
  .card-back { background: var(--card-back); }
  .back-disc {
    position: absolute;
    left: -40px; top: 30px;
    width: 260px; height: 260px;
    border-radius: 50%;
    background: var(--mark-faint);
  }
  .back-name {
    position: absolute;
    right: 34px; bottom: 44px;
    text-align: center;
    font-weight: 800;
    font-size: 44px;
    line-height: 1;
    letter-spacing: -0.01em;
  }
  .back-name span { display: block; }
  .back-name .joiner { font-size: 16px; letter-spacing: .1em; margin: 4px 0; }
</style>
</head>
<body>
  <section class="card card-front">
    <div class="wordmark">
      <span class="wordmark-dot"></span>
      <span class="wordmark-name">IRON AND GRIT</span>
    </div>
    <div class="details">
      <div class="person">
        <div class="person-name">DANIEL REYES</div>
        <div class="person-role">CEO/Founder</div>
      </div>
      <div class="divider"></div>
      <ul class="contact">
        <li><svg viewBox="0 0 24 24"><path d="M6.6 10.8a15 15 0 0 0 6.6 6.6l2.2-2.2a1 1 0 0 1 1-.25 11.4 11.4 0 0 0 3.6.57 1 1 0 0 1 1 1V20a1 1 0 0 1-1 1A17 17 0 0 1 3 4a1 1 0 0 1 1-1h3.5a1 1 0 0 1 1 1c0 1.25.2 2.45.57 3.57a1 1 0 0 1-.25 1z"/></svg>(555) 014 2290</li>
        <li><svg viewBox="0 0 24 24"><path d="M2 5h20v14H2zm2 2v.4l8 5 8-5V7z"/></svg>hello@ironandgrit.com</li>
        <li><svg viewBox="0 0 24 24"><circle cx="12" cy="12" r="10"/></svg>www.ironandgrit.com</li>
      </ul>
    </div>
    <p class="address">418 W Harbor Avenue Millbrook County 7402</p>
  </section>

  <section class="card card-back">
    <div class="back-disc"></div>
    <div class="back-name">
      <span>IRON</span>
      <span class="joiner">AND</span>
      <span>GRIT</span>
    </div>
  </section>
</body>
</html>
```